依頼詳細
中古車販売店「そよぎ堂」の名刺のデザインをお願いしたいです。
今年40歳になりました、私が使います。
好きな色はライムグリーンですが、最近は水色も好きなので候補に入れました。
ただ、必ずしも色を入れたいわけではなく、デザイン次第ではモノクロも大歓迎です。
あまりごちゃごちゃせず、シンプルなものが嬉しいですね。
正式には「そよぎ堂」ですが、「SOYOGIDO」というロゴもございます。
どちらでもけっこうです。
記載項目
表面に、
屋号:そよぎ堂 もしくは SOYOGIDO
私の氏名:土屋文雄
郵便番号:612-4376
住所:京都市南区吉祥院松尾町37-2
TEL:075-431-6029
FAX:075-431-6030
携帯電話:080-7392-6804
URL:https://soyogi-do.example
メール:info@soyogi-do.example

を記載したいです。
また、デザインによってはロゴの挿入もお願いしたいです。
希望イメージ
シンプル 複雑
単色 カラフル
暗い 明るい
日常 高級
遊び心 厳粛
未来的 伝統的
女性的 男性的
希望する色
緑系、水色系、無彩色系
納品ファイル
• 高解像度JPG (.jpg)
• イラストレーター形式 (.ai)
補足説明
ロゴは3つあるうちの一番下、黒一色のものをお使いください。
■ 選んだ理由

裏面に地図が入っていたり、わかりやすく実用的だと思ったからです。

■ 提案者全員のお礼・コメント

多数のご応募、ありがとうございました!

```html
<!DOCTYPE html>
<html lang="ja">
<head>
<meta charset="UTF-8">
<title>そよぎ堂 名刺デザイン案</title>
<link rel="stylesheet" href="https://fonts.googleapis.com/css2?family=Noto+Sans+JP:wght@400;500;700&family=Montserrat:wght@700;800&display=swap">
<style>
  :root {
    --paper: #ffffff;
    --ink: #1d1d1d;
    --ink-soft: #3a3a3a;
    --card-border: #c9c9c9;
    --lime: #7cc96a;
    --lime-soft: #b8e2a8;
    --sky: #5bbde6;
    --sky-soft: #a9dcf2;
  }
  * { box-sizing: border-box; margin: 0; padding: 0; }
  html, body {
    width: 849px;
    height: 1200px;
    overflow: hidden;
    background: var(--paper);
  }
  .sheet {
    position: relative;
    width: 849px;
    height: 1200px;
  }
  .card {
    position: absolute;
    left: 225px;
    width: 400px;
    height: 236px;
    background: var(--paper);
    border: 1px solid var(--card-border);
    font-family: "Noto Sans JP", sans-serif;
    color: var(--ink);
  }
  .card--lime { top: 332px; --accent: var(--lime); --accent-soft: var(--lime-soft); }
  .card--sky  { top: 586px; --accent: var(--sky);  --accent-soft: var(--sky-soft); }

  .brand {
    position: absolute;
    left: 22px;
    top: 26px;
    display: flex;
    align-items: center;
    gap: 6px;
  }
  .brand__mark {
    width: 13px;
    height: 13px;
    background: var(--ink);
  }
  .brand__name {
    font-family: "Montserrat", sans-serif;
    font-weight: 800;
    font-size: 12px;
    letter-spacing: 0.04em;
    color: var(--ink);
  }

  .person-name {
    position: absolute;
    left: 130px;
    top: 82px;
    font-size: 26px;
    font-weight: 500;
    letter-spacing: 0.14em;
    color: var(--ink);
  }

  .shop-name {
    position: absolute;
    left: 22px;
    top: 130px;
    font-size: 14px;
    font-weight: 700;
    letter-spacing: 0.04em;
  }
  .rule {
    position: absolute;
    left: 22px;
    top: 152px;
    width: 356px;
    height: 2px;
    background: var(--accent);
  }
  .vehicles {
    position: absolute;
    right: 22px;
    top: 138px;
    width: 96px;
    height: 13px;
    background: linear-gradient(90deg, var(--accent-soft), var(--accent));
    border-radius: 6px 6px 0 0;
  }

  .contact {
    position: absolute;
    left: 22px;
    top: 158px;
    font-size: 8px;
    line-height: 1.45;
    color: var(--ink-soft);
    list-style: none;
  }
</style>
</head>
<body>
<main class="sheet">

  <section class="card card--lime">
    <div class="brand">
      <span class="brand__mark"></span>
      <span class="brand__name">SOYOGIDO</span>
    </div>
    <p class="person-name">土屋 文雄</p>
    <p class="shop-name">そよぎ堂</p>
    <div class="vehicles" role="img" aria-label="並んだ車のイラスト(ライムグリーン)"></div>
    <div class="rule"></div>
    <ul class="contact">
      <li>〒612-4376　京都市南区吉祥院松尾町37-2</li>
      <li>TEL：075-431-6029　FAX：075-431-6030</li>
      <li>携帯電話：080-7392-6804</li>
      <li>URL：https://soyogi-do.example　MAIL：info@soyogi-do.example</li>
    </ul>
  </section>

  <section class="card card--sky">
    <div class="brand">
      <span class="brand__mark"></span>
      <span class="brand__name">SOYOGIDO</span>
    </div>
    <p class="person-name">土屋 文雄</p>
    <p class="shop-name">そよぎ堂</p>
    <div class="vehicles" role="img" aria-label="並んだ車のイラスト(水色)"></div>
    <div class="rule"></div>
    <ul class="contact">
      <li>〒612-4376　京都市南区吉祥院松尾町37-2</li>
      <li>TEL：075-431-6029　FAX：075-431-6030</li>
      <li>携帯電話：080-7392-6804</li>
      <li>URL：https://soyogi-do.example　MAIL：info@soyogi-do.example</li>
    </ul>
  </section>

</main>
</body>
</html>
```